Brightpath Dentistry - Flyer - Modern & Eye catching campaign flyer

Need front & back side full page flyer designs for both 1) Grand opening 2) On-going campaign.

Attached the new dental office logo.
Attached our other dental clinic flyer designs for content.

Target Market(s)

Cosmetic dentistry

Industry/Entity Type

Health Care

Requirements
Must have
• decent, modern and eye catching marketing flyers.
Nice to have
• - Nice space
• - Highlight phone number
• - Highlight special features like convenient hours, call or text, for all ages, digital facility, etc
Should not have
• - Don't want to fill the flyer with too much wordings
• - Too many colors

```html
<!DOCTYPE html>
<html lang="en">
<head>
<meta charset="utf-8">
<title>Brightpath Dentistry Flyers</title>
<link href="https://fonts.googleapis.com/css2?family=Open+Sans:wght@400;600;700;800&family=Roboto+Condensed:wght@400;700&display=swap" rel="stylesheet">
<style>
:root{
  --stage:#d6d6d8;
  --navy:#12325f;
  --blue:#2f7dbd;
  --sky:#5aaee0;
  --brand:#2a9fd6;
  --orange:#f26b21;
  --white:#ffffff;
  --ink:#1d3557;
  --grey:#4a4a4a;
}
*{margin:0;padding:0;box-sizing:border-box}
html,body{width:1200px;height:900px;overflow:hidden;background:var(--stage);font-family:"Open Sans",Arial,sans-serif}
.flyer{position:absolute;top:80px;width:506px;height:728px;background:var(--white);box-shadow:0 6px 14px rgba(0,0,0,.18);overflow:hidden}
.flyer-front{left:57px}
.flyer-back{left:645px}
.flyer-bg{position:absolute;inset:0}
.abs{position:absolute}
.brand{top:12px;right:12px;display:flex;align-items:center;gap:8px;color:var(--brand);font-weight:700;font-size:21px;white-space:nowrap}
.brand-dot{width:16px;height:16px;border-radius:50%;background:var(--brand)}
.headline{left:20px;top:350px;color:var(--white);font-weight:800;font-size:32px;line-height:1;letter-spacing:.3px}
.headline span{display:block;color:var(--orange);margin-top:4px}
.offers{left:20px;top:421px;display:flex;gap:24px;color:var(--white);font-size:10px;white-space:nowrap}
.offers li{list-style:none;display:flex;align-items:center;gap:4px}
.tick{color:var(--orange);font-weight:700;font-size:12px}
.section-title{color:var(--orange);font-weight:700;font-size:12.5px}
.body-copy{color:var(--white);font-size:9.8px;line-height:1.4;margin-top:7px}
.block-close{left:20px;top:456px;width:462px}
.block-family{left:20px;top:530px;width:470px}
.call{right:16px;top:670px;text-align:right;font-family:"Roboto Condensed",Arial,sans-serif}
.call-label{color:var(--ink);font-weight:700;font-size:24px;line-height:1}
.call-number{color:var(--orange);font-weight:700;font-size:27px;line-height:1.05}
.footer{left:20px;top:708px;display:flex;align-items:center;font-size:9.5px;color:var(--grey);white-space:nowrap}
.footer .sep{width:1px;height:16px;background:#ccc;margin:0 20px}
.footer svg{margin-right:5px}
.badge{left:34px;top:594px;width:98px;height:98px;border-radius:22px;background:var(--orange);border:3px solid var(--white);display:flex;align-items:center;justify-content:center;text-align:center;color:var(--white);font-weight:700;font-size:10px;line-height:1.3}
.services-title{left:20px;top:320px;color:var(--orange);font-weight:700;font-size:12.5px}
.services{left:0;top:348px;width:506px;display:grid;grid-template-columns:repeat(4,1fr);row-gap:20px}
.service{display:flex;flex-direction:column;align-items:center;text-align:center;color:var(--white);font-size:10.5px;line-height:1.25;height:76px}
.service-icon{width:36px;height:36px;border-radius:50%;background:var(--orange);display:flex;align-items:center;justify-content:center;margin-bottom:7px;box-shadow:0 0 0 2px rgba(255,255,255,.25)}
.welcome{left:18px;top:536px;width:392px;height:36px;border-radius:18px;background:var(--orange);color:var(--white);font-weight:700;font-size:19.5px;display:flex;align-items:center;justify-content:center;letter-spacing:.2px}
.valid{left:20px;top:585px;color:var(--white);font-family:"Roboto Condensed",Arial,sans-serif;white-space:nowrap}
.valid-main{font-size:21px;font-weight:700;line-height:1.1}
.valid-sub{font-family:"Open Sans",Arial,sans-serif;font-size:17px;line-height:1.3}
</style>
</head>
<body>

<section class="flyer flyer-front">
  <svg class="flyer-bg" width="506" height="728" viewBox="0 0 506 728">
    <defs>
      <linearGradient id="familyTones" x1="0" y1="0" x2="1" y2="1">
        <stop offset="0" stop-color="#f4f2f0"/>
        <stop offset=".5" stop-color="#e7d2bf"/>
        <stop offset="1" stop-color="#f6efe6"/>
      </linearGradient>
      <linearGradient id="panelFront" x1="0" y1="0" x2="1" y2="1">
        <stop offset="0" stop-color="#12325f"/>
        <stop offset="1" stop-color="#2f7dbd"/>
      </linearGradient>
      <linearGradient id="friendsTones" x1="0" y1="0" x2="1" y2="1">
        <stop offset="0" stop-color="#e9dccb"/>
        <stop offset="1" stop-color="#b69879"/>
      </linearGradient>
    </defs>
    <rect x="0" y="0" width="506" height="330" fill="url(#familyTones)" role="img" aria-label="Photo of a smiling family of four"/>
    <path d="M0,190 C130,240 260,320 380,310 C440,304 480,262 506,230 L506,728 L0,728Z" fill="var(--sky)"/>
    <path d="M0,202 C130,252 260,332 380,322 C440,316 480,274 506,242 L506,728 L0,728Z" fill="url(#panelFront)"/>
    <path d="M0,668 C160,676 340,636 506,612 L506,728 L0,728Z" fill="var(--orange)"/>
    <path d="M0,676 C160,684 340,644 506,620 L506,728 L0,728Z" fill="var(--white)"/>
    <circle cx="423" cy="292" r="68" fill="url(#friendsTones)" stroke="var(--orange)" stroke-width="5" role="img" aria-label="Photo of two women chatting over coffee"/>
  </svg>

  <div class="abs brand"><span class="brand-dot"></span>Brightpath Dentistry</div>

  <h1 class="abs headline">GRAND OPENING<span>SPECIALS</span></h1>

  <ul class="abs offers">
    <li><span class="tick">✓</span>Free Kids Dental Screening</li>
    <li><span class="tick">✓</span>$25 Adults Dental Screening</li>
    <li><span class="tick">✓</span>15% Off On Treatment Plan</li>
  </ul>

  <div class="abs block-close">
    <h2 class="section-title">Looking For Dentist Close To Home?</h2>
    <p class="body-copy">Come and See Us for Professional Services and Care. Our dentists and staff are experts in the field of advanced dentistry and will help you achieve your perfect smile.</p>
  </div>

  <div class="abs block-family">
    <h2 class="section-title">Family &amp; Cosmetic dentistry</h2>
    <p class="body-copy">Filled with entertainment devices for patient comfort. Same-day appointment for Dental Emergencies<br>Helping community with routine free kids dental screening.</p>
  </div>

  <div class="abs badge">ALL<br>INSURANCES<br>ACCEPTED</div>

  <div class="abs call">
    <div class="call-label">Call Or Text Us Now:</div>
    <div class="call-number">555.014.2290</div>
  </div>

  <div class="abs footer">
    <svg width="10" height="10" viewBox="0 0 10 10"><circle cx="5" cy="5" r="5" fill="var(--orange)"/></svg>www.brightpathdds.com
    <span class="sep"></span>
    <svg width="10" height="8" viewBox="0 0 10 8"><rect width="10" height="8" rx="1" fill="var(--orange)"/><path d="M0,0 L5,4 L10,0" stroke="#fff" fill="none"/></svg>info@brightpathdds.com
  </div>
</section>

<section class="flyer flyer-back">
  <svg class="flyer-bg" width="506" height="728" viewBox="0 0 506 728">
    <defs>
      <linearGradient id="smileTones" x1="0" y1="0" x2="1" y2="1">
        <stop offset="0" stop-color="#9a8577"/>
        <stop offset=".5" stop-color="#d9c7bd"/>
        <stop offset="1" stop-color="#7c6a60"/>
      </linearGradient>
      <linearGradient id="panelBack" x1="0" y1="0" x2="1" y2="1">
        <stop offset="0" stop-color="#12325f"/>
        <stop offset="1" stop-color="#2f7dbd"/>
      </linearGradient>
    </defs>
    <rect x="0" y="0" width="506" height="330" fill="url(#smileTones)" role="img" aria-label="Photo of a family holding up large smile prints"/>
    <path d="M0,198 C130,250 260,320 380,308 C440,302 480,250 506,218 L506,728 L0,728Z" fill="var(--sky)"/>
    <path d="M0,210 C130,262 260,332 380,320 C440,314 480,262 506,230 L506,728 L0,728Z" fill="url(#panelBack)"/>
    <path d="M0,668 C160,676 340,636 506,612 L506,728 L0,728Z" fill="var(--orange)"/>
    <path d="M0,676 C160,684 340,644 506,620 L506,728 L0,728Z" fill="var(--white)"/>
  </svg>

  <h2 class="abs services-title">Our Services</h2>

  <div class="abs services">
    <div class="service"><span class="service-icon"><svg width="18" height="20" viewBox="0 0 18 20"><path d="M9,3 C7,0 1,0 1,6 C1,11 3,12 4,18 C5,21 7,19 7,14 C7,12 11,12 11,14 C11,19 13,21 14,18 C15,12 17,11 17,6 C17,0 11,0 9,3Z" fill="#fff"/></svg></span>Root Canal<br>Therapy</div>
    <div class="service"><span class="service-icon"><svg width="22" height="16" viewBox="0 0 22 16"><rect x="1" y="2" width="20" height="5" rx="2" fill="#fff"/><rect x="1" y="9" width="20" height="5" rx="2" fill="#fff"/></svg></span>Dentures</div>
    <div class="service"><span class="service-icon"><svg width="20" height="18" viewBox="0 0 20 18"><path d="M10,2 C8,0 4,0 4,4 C4,7 5,8 6,11 L14,11 C15,8 16,7 16,4 C16,0 12,0 10,2Z" fill="#fff"/><path d="M1,14 L8,14 L12,12 L19,12 L19,17 L1,17Z" fill="#fff"/></svg></span>Clear Aligners<br>(Invisible Braces)</div>
    <div class="service"><span class="service-icon"><svg width="20" height="20" viewBox="0 0 20 20"><path d="M10,5 C8,3 4,3 4,7 C4,11 6,12 6,17 C7,19 8,18 9,15 L11,15 C12,18 13,19 14,17 C14,12 16,11 16,7 C16,3 12,3 10,5Z" fill="#fff"/><path d="M2,2 L4,4 M18,2 L16,4 M10,0 L10,2" stroke="#fff" stroke-width="1.5"/></svg></span>Laser Teeth<br>Whitening</div>
    <div class="service"><span class="service-icon"><svg width="16" height="22" viewBox="0 0 16 22"><path d="M1,3 C1,0 15,0 15,3 C15,7 12,8 8,8 C4,8 1,7 1,3Z" fill="#fff"/><rect x="6" y="9" width="4" height="12" rx="1" fill="#fff"/></svg></span>Implants</div>
    <div class="service"><span class="service-icon"><svg width="22" height="16" viewBox="0 0 22 16"><path d="M2,4 C2,0 20,0 20,4 L20,10 C20,16 2,16 2,10Z" fill="none" stroke="#fff" stroke-width="2.5"/><rect x="6" y="5" width="10" height="5" rx="1" fill="#fff"/></svg></span>Night Guards</div>
    <div class="service"><span class="service-icon"><svg width="20" height="20" viewBox="0 0 20 20"><path d="M9,4 C7,1 2,1 2,6 C2,10 4,11 5,17 C6,20 7,18 8,14 L10,14 C11,18 12,20 13,17 C14,11 16,10 16,6 C16,1 11,1 9,4Z" fill="#fff"/><path d="M17,1 L18,3 L20,4 L18,5 L17,7 L16,5 L14,4 L16,3Z" fill="#fff"/></svg></span>Veneers</div>
    <div class="service"><span class="service-icon"><svg width="18" height="20" viewBox="0 0 18 20"><path d="M2,1 L16,1 L16,8 L2,8Z" fill="#fff"/><path d="M3,10 L15,10 C15,14 13,15 12,19 L10,19 L9,15 L8,19 L6,19 C5,15 3,14 3,10Z" fill="#fff"/></svg></span>Crown &amp; Bridge</div>
  </div>

  <div class="abs welcome">NEW PATIENTS ARE WELCOME!</div>

  <div class="abs valid">
    <div class="valid-main">OPENING SPECIAL OFFERS VALID UNTIL JUNE 15, 2017</div>
    <div class="valid-sub">by Appointment only</div>
  </div>

  <div class="abs call">
    <div class="call-label">Call Or Text Us Now:</div>
    <div class="call-number">555.014.2290</div>
  </div>

  <div class="abs footer">
    <svg width="10" height="10" viewBox="0 0 10 10"><circle cx="5" cy="5" r="5" fill="var(--orange)"/></svg>www.brightpathdds.com
    <span class="sep"></span>
    <svg width="10" height="8" viewBox="0 0 10 8"><rect width="10" height="8" rx="1" fill="var(--orange)"/><path d="M0,0 L5,4 L10,0" stroke="#fff" fill="none"/></svg>info@brightpathdds.com
  </div>
</section>

</body>
</html>
```